We currently have a good logo and we want business cards that can display our logo but also represent our industry - telecom construction - We are a construction company specializing in telecom construction such as installation of fiber optic cable throughout cities and across the country. Nationwide services
We are large enough to handle most any project yet small enough to be a flexible partner and resource.

Target Market(s)

U.S. based telecom carriers and providers

Industry/Entity Type

Construction

Contact Information for Business Card

Business cards should include our logo, phone number and website address. Also, including some information as to our core services would be good.

Colors

Designer to choose colors to be used in the design.

Requirements
Must have
• Colors based on logo
• Must use our logo
• Logo, name, email, website address, phone number
• Tovasco Conduit
• Brent Halvik
• Director of Business Development
• (555) 271-0386
• www.TVSQ-example.com
Nice to have
• Construction services including:
• Small Cell Construction
• Boring/Drilling
• Plowing / Trenching
• Conduit installation
• Fiber pulling
• splicing
• building entries
• Aerial construction
• Aerial Make Ready
• Make Ready Engineering
Should not have
• We are open to ideas

```html
<!DOCTYPE html>
<html lang="en">
<head>
<meta charset="utf-8">
<title>Tovasco Conduit – Business Cards</title>
<link href="https://fonts.googleapis.com/css2?family=Poppins:wght@400;500;600;700&display=swap" rel="stylesheet">
<style>
  :root {
    --bg: #2a2a2a;
    --card: #ffffff;
    --blue: #1a7fd4;
    --blue-deep: #0b5cb0;
    --ink: #3c3c3c;
    --rule: #6a6a6a;
  }
  * { box-sizing: border-box; margin: 0; padding: 0; }
  html, body { width: 1200px; height: 880px; overflow: hidden; }
  body {
    background: var(--bg);
    font-family: "Poppins", sans-serif;
    color: var(--ink);
    position: relative;
  }
  .card {
    position: absolute;
    width: 560px;
    height: 320px;
    background: var(--card);
    border-radius: 22px;
    overflow: hidden;
    box-shadow: 0 14px 30px rgba(0,0,0,.45);
  }
  .card::after {
    content: "";
    position: absolute;
    top: 0; right: 0;
    width: 10px; height: 100%;
    background: linear-gradient(180deg, var(--blue), var(--blue-deep));
  }
  .card--services { left: 60px; top: 90px; }
  .card--contact { left: 580px; top: 470px; }

  .brand {
    position: absolute;
    display: flex;
    align-items: center;
    gap: 12px;
    font-weight: 700;
    font-size: 30px;
    line-height: 1.05;
    color: var(--blue);
  }
  .brand__dot {
    width: 16px; height: 16px;
    border-radius: 50%;
    background: var(--blue);
    flex: none;
  }
  .brand__name { display: block; }
  .card--services .brand { left: 340px; top: 78px; }
  .card--contact .brand { right: 50px; top: 34px; }

  .services { position: absolute; left: 46px; top: 62px; width: 270px; }
  .services__title {
    font-size: 17px;
    font-weight: 600;
    color: var(--blue);
    letter-spacing: .5px;
    margin-bottom: 10px;
    white-space: nowrap;
  }
  .services__list { list-style: none; }
  .services__list li {
    font-size: 13.5px;
    line-height: 19px;
    padding-left: 22px;
    position: relative;
  }
  .services__list li::before {
    content: "";
    position: absolute;
    left: 2px; top: 6px;
    width: 8px; height: 8px;
    border-radius: 50%;
    background: var(--blue);
  }

  .rule { position: absolute; height: 1px; background: var(--rule); }
  .rule--top { left: 290px; right: 40px; top: 128px; }
  .rule--bottom { left: 40px; right: 40px; top: 282px; }

  .person { position: absolute; left: 40px; top: 96px; }
  .person__name {
    font-size: 21px;
    font-weight: 600;
    color: var(--blue);
    letter-spacing: .5px;
    line-height: 1.1;
  }
  .person__role { font-size: 13px; line-height: 1.3; white-space: nowrap; }

  .address { position: absolute; left: 40px; top: 156px; font-size: 13px; line-height: 18px; }
  .address__company { font-weight: 600; }

  .contacts { position: absolute; left: 40px; top: 216px; list-style: none; }
  .contacts li {
    display: flex; align-items: center; gap: 8px;
    font-size: 13px; line-height: 20px;
  }
  .contacts svg { width: 15px; height: 15px; flex: none; }
</style>
</head>
<body>

  <section class="card card--services">
    <div class="services">
      <h2 class="services__title">CONSTRUCTION SERVICES</h2>
      <ul class="services__list">
        <li>Small Cell Construction</li>
        <li>Boring/Drilling</li>
        <li>Plowing / Trenching</li>
        <li>Conduit installation</li>
        <li>Fiber pulling</li>
        <li>Splicing</li>
        <li>Building entries</li>
        <li>Aerial construction</li>
        <li>Aerial Make Ready</li>
        <li>Make Ready Engineering</li>
      </ul>
    </div>
    <div class="brand"><span class="brand__dot"></span><span class="brand__name">Tovasco<br>Conduit</span></div>
  </section>

  <section class="card card--contact">
    <div class="brand"><span class="brand__dot"></span><span class="brand__name">Tovasco<br>Conduit</span></div>
    <div class="rule rule--top"></div>

    <div class="person">
      <h1 class="person__name">BRENT HALVIK</h1>
      <p class="person__role">Director of Business Development</p>
    </div>

    <div class="address">
      <p class="address__company">Tovasco Conduit</p>
      <p>PO BOX 480 Harlow Lane,</p>
      <p>2nd street Lindmere</p>
    </div>

    <ul class="contacts">
      <li>
        <svg viewBox="0 0 16 16" aria-hidden="true"><circle cx="8" cy="8" r="8" fill="#1a7fd4"/><path d="M5.2 4.2l1.4-.3.8 2-1 .7a5 5 0 0 0 2.9 2.9l.7-1 2 .8-.3 1.4c-3.6.3-6.8-2.9-6.5-6.5z" fill="#fff"/></svg>
        (555) 271-0386
      </li>
      <li>
        <svg viewBox="0 0 16 16" aria-hidden="true"><circle cx="8" cy="8" r="8" fill="#1a7fd4"/><rect x="4" y="5.2" width="8" height="5.6" rx=".6" fill="#fff"/><path d="M4.3 5.6L8 8.4l3.7-2.8" stroke="#1a7fd4" stroke-width=".8" fill="none"/></svg>
        info@tvsq-example.com
      </li>
      <li>
        <svg viewBox="0 0 16 16" aria-hidden="true"><circle cx="8" cy="8" r="8" fill="#1a7fd4"/><circle cx="8" cy="8" r="4" stroke="#fff" stroke-width=".9" fill="none"/><path d="M4 8h8M8 4c-1.8 2.4-1.8 5.6 0 8M8 4c1.8 2.4 1.8 5.6 0 8" stroke="#fff" stroke-width=".8" fill="none"/></svg>
        www.TVSQ-example.com
      </li>
    </ul>

    <div class="rule rule--bottom"></div>
  </section>

</body>
</html>
```